Eye-Catching, Direct Marketing Residential Painting Flyer!

I am run a residential painting business and am looking for a flyer to be designed to mailout to potential customers.
I want the copy/wording to be designed similar to this flyer.

It's important that the person reading the flyer gets the benefits we're promoting which is why I want the wording/copy to be almost identical to the flyer attached.

However, the structure will be different. The flyer will be a postcard thick, 5 x11.5.
Double sided.

The name of the company is Brightwall Coaters.

I would also like the prominent colour to either be light green or orange.

Target Market(s)

Home Owners between the age of 45-80.

Industry/Entity Type

Painting And Decorating

Font styles to use
Serif

Colors
f68d4d
faa54b
f78f20
f37122
9bcb3c
abd037
cadf82

Requirements
Must have
• Excellent Eye-Catching Design
• Benefits Visibly Promoted
• Action Taking Incentive- Call Now for FREE Window Cleaning and FREE Painting Estimate
Should not have
• Crowded wording

```html
<!DOCTYPE html>
<html lang="en">
<head>
<meta charset="utf-8">
<title>Brightwall Coaters – Postcard</title>
<link href="https://fonts.googleapis.com/css2?family=Raleway:wght@800;900&family=Cabin:wght@400;600&family=Roboto+Condensed:wght@400;700&display=swap" rel="stylesheet">
<style>
  :root{
    --green:#9bcb3c;
    --green-mid:#abd037;
    --green-pale:#cadf82;
    --ink:#333333;
    --slate:#58595b;
    --panel:#e6e7e8;
    --paper:#ffffff;
    --backdrop:#d9d9d9;
  }
  *{margin:0;padding:0;box-sizing:border-box;}
  html,body{width:1200px;height:801px;overflow:hidden;background:var(--backdrop);}
  .canvas{position:relative;width:1200px;height:801px;}
  .card{position:absolute;left:269px;width:662px;height:287px;background:var(--paper);overflow:hidden;box-shadow:0 4px 10px rgba(0,0,0,.35);}
  .card--front{top:98px;}
  .card--back{top:416px;}
  .card svg.shapes{position:absolute;left:0;top:0;}
  .abs{position:absolute;}

  /* front */
  .brand{left:0;width:394px;top:36px;text-align:center;font-family:"Cabin",sans-serif;font-weight:600;font-size:18px;color:var(--green);letter-spacing:.2px;}
  .headline{left:0;width:394px;top:67px;text-align:center;font-family:"Raleway",sans-serif;font-weight:900;font-size:21px;line-height:25px;color:var(--green-mid);letter-spacing:.3px;}
  .headline .headline__lead{color:var(--green-pale);}
  .offer-tag{left:36px;top:155px;font-family:"Roboto Condensed",sans-serif;font-weight:700;font-size:14px;color:var(--green-pale);}
  .offer{font-family:"Cabin",sans-serif;font-size:10px;line-height:12.5px;color:var(--ink);font-weight:600;}
  .offer em{font-style:normal;color:var(--green);}
  .offer .offer__count{font-size:12px;font-weight:400;}
  .offer--left{left:37px;top:187px;width:150px;}
  .offer--right{left:214px;top:174px;width:165px;}
  .strap{left:42px;top:265px;font-family:"Raleway",sans-serif;font-weight:900;font-size:12px;color:#fff;letter-spacing:.3px;}
  .burst-text{left:346px;top:110px;width:120px;text-align:center;color:#fff;font-family:"Roboto Condensed",sans-serif;transform:rotate(-12deg);line-height:1.05;}
  .burst-text .s{font-size:10px;display:block;}
  .burst-text .l{font-size:15px;display:block;}

  /* back */
  .pair{left:182px;width:149px;text-align:center;font-family:"Roboto Condensed",sans-serif;color:var(--ink);}
  .pair h3{font-family:"Cabin",sans-serif;font-weight:400;font-size:10.5px;color:var(--green);line-height:13px;}
  .pair p{font-size:7.2px;line-height:9.5px;padding:0 10px;}
  .pair--one{top:13px;}
  .pair--two{top:113px;}
  .estimates{left:134px;top:236px;font-family:"Raleway",sans-serif;font-weight:900;font-size:15px;color:var(--green);letter-spacing:.4px;}
  .contact{left:40px;top:262px;font-family:"Raleway",sans-serif;font-weight:900;font-size:17px;color:#fff;letter-spacing:.3px;}
</style>
</head>
<body>
<div class="canvas">

  <!-- FRONT -->
  <section class="card card--front">
    <svg class="shapes" width="662" height="287" viewBox="0 0 662 287">
      <defs>
        <linearGradient id="deckTone" x1="0" y1="0" x2="1" y2="0.35">
          <stop offset="0" stop-color="#b9a27c"/>
          <stop offset="0.45" stop-color="#a48661"/>
          <stop offset="0.55" stop-color="#8b4a2c"/>
          <stop offset="1" stop-color="#6e3420"/>
        </linearGradient>
      </defs>
      <circle cx="197" cy="24" r="11" fill="none" stroke="var(--green)" stroke-width="2.5"/>
      <rect x="0" y="38" width="440" height="2" fill="var(--green)"/>
      <rect x="0" y="57" width="430" height="2" fill="var(--green)"/>
      <path d="M0,150 L165,151 L158,156 L170,159 L156,163 L166,168 L150,172 L160,176 L0,178 Z" fill="var(--green)"/>
      <rect x="186" y="185" width="1" height="58" fill="#999"/>
      <rect x="189" y="180" width="1" height="68" fill="#bbb"/>
      <rect x="0" y="260" width="662" height="27" fill="var(--green)"/>
      <path d="M440,0 C382,70 377,200 444,287 L662,287 L662,0 Z" fill="var(--green-pale)"/>
      <path d="M448,0 C390,70 385,200 452,287 L662,287 L662,0 Z" fill="var(--green)"/>
      <path d="M456,0 C398,70 393,200 460,287 L662,287 L662,0 Z" fill="url(#deckTone)" role="img" aria-label="Photo of a wooden deck half restained, with a stain can, brush and gloves"/>
      <polygon transform="translate(406,148) scale(0.93)" fill="var(--slate)" stroke="#fff" stroke-width="1.5"
        points="62,0 51,10.1 57.3,23.7 43.2,28.9 43.8,43.8 28.9,43.2 23.7,57.3 10.1,51 0,62 -10.1,51 -23.7,57.3 -28.9,43.2 -43.8,43.8 -43.2,28.9 -57.3,23.7 -51,10.1 -62,0 -51,-10.1 -57.3,-23.7 -43.2,-28.9 -43.8,-43.8 -28.9,-43.2 -23.7,-57.3 -10.1,-51 0,-62 10.1,-51 23.7,-57.3 28.9,-43.2 43.8,-43.8 43.2,-28.9 57.3,-23.7 51,-10.1"/>
    </svg>

    <div class="abs brand">BRIGHTWALL COATERS</div>
    <h1 class="abs headline"><span class="headline__lead">WE MAKE YOUR HOME LOOK</span><br>CLEAN, FRESH &amp; BEAUTIFUL<br>AGAIN!</h1>
    <div class="abs offer-tag">SPECIAL OFFER!</div>
    <p class="abs offer offer--left">If you are one of the<br><em class="offer__count">first 17 exterior projects</em><br>that book with us, you will receive a complimentary<br><em>window cleaning!</em></p>
    <p class="abs offer offer--right">If you are one of the<br><em class="offer__count">first 13 exterior projects</em><br>that book with us, you will receive a complimentary<br><em>interior design consultation by a professional interior designer!</em></p>
    <div class="abs strap">TAKE CONTROL OF HOW YOUR HOME LOOKS!</div>
    <div class="abs burst-text"><span class="s">Call Now</span><span class="l">for FREE</span><span class="s">Window Cleaning</span><span class="l">and FREE</span><span class="s">Painting Estimate</span></div>
  </section>

  <!-- BACK -->
  <section class="card card--back">
    <svg class="shapes" width="662" height="287" viewBox="0 0 662 287">
      <defs>
        <linearGradient id="wallTone" x1="0" y1="0" x2="0" y2="1">
          <stop offset="0" stop-color="#a2735a"/>
          <stop offset="0.5" stop-color="#cfc6bb"/>
          <stop offset="1" stop-color="#9a8f7c"/>
        </linearGradient>
        <linearGradient id="roomTone" x1="0" y1="0" x2="1" y2="1">
          <stop offset="0" stop-color="#d8d4d2"/>
          <stop offset="1" stop-color="#b7b0ac"/>
        </linearGradient>
        <linearGradient id="stepTone" x1="0" y1="0" x2="0" y2="1">
          <stop offset="0" stop-color="#9aa19c"/>
          <stop offset="1" stop-color="#6f7771"/>
        </linearGradient>
        <filter id="soft" x="-10%" y="-10%" width="120%" height="130%"><feDropShadow dx="0" dy="2" stdDeviation="1.5" flood-opacity=".3"/></filter>
      </defs>
      <path d="M0,0 L118,0 C165,15 178,80 170,110 C160,150 150,190 120,220 C90,250 40,262 0,258 Z" fill="var(--green)"/>
      <path d="M0,0 L112,0 C158,18 170,80 162,110 C152,150 142,188 114,214 C86,242 38,254 0,250 Z" fill="url(#wallTone)" role="img" aria-label="Photos of a wall being repainted and a peeling wooden fence"/>
      <circle cx="126" cy="73" r="50" fill="var(--green)"/>
      <circle cx="126" cy="73" r="45" fill="url(#roomTone)" role="img" aria-label="Photo of a freshly painted interior room"/>
      <circle cx="103" cy="160" r="52" fill="var(--green)"/>
      <circle cx="103" cy="160" r="47" fill="url(#stepTone)" role="img" aria-label="Photo of freshly painted grey steps"/>
      <rect x="182" y="10" width="149" height="95" rx="6" fill="var(--panel)" filter="url(#soft)"/>
      <rect x="182" y="110" width="149" height="96" rx="6" fill="var(--panel)" filter="url(#soft)"/>
      <rect x="572" y="27" width="58" height="57" fill="none" stroke="#555" stroke-width="1"/>
      <rect x="437" y="186" width="192" height="1" fill="#555"/>
      <rect x="437" y="213" width="192" height="1" fill="#555"/>
      <rect x="437" y="240" width="192" height="1" fill="#555"/>
      <rect x="0" y="259" width="662" height="28" fill="var(--green)"/>
    </svg>

    <div class="abs pair pair--one">
      <h3>Problem:</h3>
      <p>Your deck or fence is chipping or peeling, and looks old and faded.</p>
      <h3>Solution:</h3>
      <p>A fresh coat of stain will protect your investment and make it look clean, fresh and Beautiful again!</p>
    </div>
    <div class="abs pair pair--two">
      <h3>Problem:</h3>
      <p>Is the colour in your interior basement, kitchen, bedrooms and bathrooms walls, doors, and trim faded or out-of-date?</p>
      <h3>Solution:</h3>
      <p>A fresh coat of paint to make your interior look clean, fresh and beautiful again!</p>
    </div>
    <div class="abs estimates">FREE ESTIMATES:</div>
    <div class="abs contact">000 - 000 - 0000 | BRIGHTWALLCOATERS.COM</div>
  </section>

</div>
</body>
</html>
```